Web Design for Small Healthcare Startup

Hello,

We are seeking a Website Design for a healthcare company focusing on mobile vaccinations, employee health and wellness services onsite at businesses, and consulting services relating to Healthcare Entities in WA state. Our company’s mission is to “To aid in a healthier workplace”. Brightpath Rovers will provide on-site wellness services to employers that simplify and streamline employee preventative health as well as onsite consulting services to help with compliance of Healthcare Entities.

We are seeking a Website Design for Brightpath Rovers, PLLC. Our company’s mission is to provide mobile health and wellness services to employers onsite at their businesses. These services include mobile vaccinations clinics for employees as well as wellness and health screenings. The company will also offer healtcare compliance consulting services for Healthcare Entities. The company was founded to bring these important healthcare services to businesses and keep employees healthy. Healthy employees are the cornerstone to a great business and we want to help orginazations achieve their goals of having a healthy productive workforce.

We are looking for a moderin website design that will need to be coded. We have attached our current logo design for reference as well as a brief questionare regarding our business for your information (not necessary to include all information). We would like something SEO friendly and easy to navigate.

Thank you!

Brightpath Rovers, PLLC

Target Market(s)

Small Businesses

Industry/Entity Type

Healthcare

Coding

Coded - Design and coding required

Number of Pages Required

1 page

Requirements
Nice to have
• SEO Friendly, Incorporate Logo

```html
<!DOCTYPE html>
<html lang="en">
<head>
<meta charset="utf-8">
<title>Brightpath Rovers, PLLC – Mobile Vaccine Clinics</title>
<link href="https://fonts.googleapis.com/css2?family=Montserrat:wght@800;900&family=Mulish:wght@400;600;700;800&display=swap" rel="stylesheet">
<style>
:root{
  --blue:#0f4aa5;
  --blue-dark:#0a3d93;
  --purple:#a0479e;
  --ink:#2b2b2b;
  --soft:#f5f4f5;
  --circle:#eef2f8;
  --footer:#1d1d1d;
  --white:#fff;
}
*{box-sizing:border-box;margin:0;padding:0}
html,body{width:1200px;height:2704px;overflow:hidden}
body{font-family:"Mulish",sans-serif;color:var(--ink);background:var(--white);position:relative}
.section{position:absolute;left:0;width:1200px}
.heading{font-family:"Montserrat",sans-serif;font-weight:900;color:var(--blue);font-size:25px;text-transform:uppercase;letter-spacing:.2px}
.heading span{color:var(--purple)}
.rule{display:block;height:3px;background:var(--blue);margin-top:6px}
.btn{display:inline-block;background:var(--purple);color:var(--white);font-family:"Montserrat",sans-serif;font-weight:800;text-transform:uppercase;text-decoration:none;font-size:13px;padding:9px 14px}
.photo{position:absolute}

/* header */
.site-header{top:0;height:102px}
.brand{position:absolute;left:133px;top:36px;display:flex;align-items:center;gap:8px;font-weight:800;font-size:19px;color:var(--blue)}
.brand i{width:14px;height:14px;border-radius:50%;background:var(--purple);display:block}
.call{position:absolute;left:727px;top:18px;display:flex;gap:10px;align-items:center}
.call small{display:block;font-size:12px;font-weight:600;text-transform:uppercase}
.call strong{display:block;font-size:17px;font-weight:600;color:var(--blue)}
.site-header .btn{position:absolute;left:919px;top:19px;font-size:12px;padding:9px 15px}
.nav{position:absolute;right:133px;top:66px;display:flex;gap:31px;font-size:14px;font-weight:700;text-transform:uppercase}
.nav a{color:var(--ink);text-decoration:none;padding-bottom:5px}
.nav a.active{color:var(--purple);border-bottom:2px solid var(--purple)}

/* hero */
.hero{top:102px;height:575px;background:linear-gradient(180deg,#4f6e55 0%,#d9dcdf 25%,#e8eaec 45%,#1f56b0 48%,#2b5fb6 52%,#dfe1e3 55%,#b9bcbf 80%,#8a8c8e 100%)}
.hero h1{position:absolute;top:205px;width:100%;text-align:center;font-family:"Montserrat",sans-serif;font-weight:900;font-size:34px;color:var(--white);text-transform:uppercase;text-shadow:0 2px 6px rgba(0,0,0,.35)}
.hero .btn{position:absolute;left:308px;top:273px;width:585px;text-align:center;font-size:18px;padding:13px 0}
.dots{position:absolute;top:531px;left:569px;display:flex;gap:6px}
.dots i{width:8px;height:8px;background:var(--white);display:block}
.dots i.on{background:var(--purple);outline:1px solid var(--white)}

/* about */
.about{top:677px;height:488px}
.about .photo{left:129px;top:43px;width:444px;height:394px;background:linear-gradient(135deg,#cfd6c4,#8aa07a 45%,#6f8fb8 70%,#c99f72)}
.about-text{position:absolute;left:615px;top:40px;width:452px;font-size:14.5px;line-height:20px;text-align:justify}
.about-text .heading{display:inline-block}
.about-text p{margin-top:20px}
.about-text .heading+p{margin-top:36px}
.about-text .btn{margin-top:27px;margin-left:2px}

/* services */
.services{top:1165px;height:519px;background:var(--soft)}
.services .photo{left:622px;top:0;width:578px;height:519px;background:radial-gradient(ellipse at 50% 40%,#e6d2be,#c7a78a 70%,#b89275)}
.services-text{position:absolute;left:130px;top:36px;width:470px;font-size:14.5px;line-height:20px}
.services-text .heading{display:inline-block}
.services-text ul{list-style:none;margin-top:18px}
.services-text li{position:relative;padding-left:30px;margin-bottom:19px}
.services-text li::before{content:"";position:absolute;left:2px;top:6px;border-left:6px solid var(--blue);border-top:4px solid transparent;border-bottom:4px solid transparent}
.services-text .btn{margin-left:3px;margin-top:4px}

/* band */
.band{top:1684px;height:243px;background:linear-gradient(90deg,#0a3e98,#0f4aa5 50%,#0a3e98);color:var(--white);text-align:center}
.band h2{font-family:"Montserrat",sans-serif;font-weight:900;font-size:24px;margin-top:57px;text-transform:uppercase}
.band p{font-size:18px;margin-top:14px}
.band .btn{margin-top:21px;font-size:15px;padding:9px 16px}

/* schedule */
.schedule{top:1927px;height:485px;text-align:center}
.schedule .heading{margin-top:44px}
.schedule .lead{font-size:14.5px;line-height:20px;margin-top:16px}
.schedule .short-rule{width:46px;height:3px;background:var(--blue);margin:23px auto 0}
.steps{position:absolute;top:184px;left:205px;display:flex;gap:24px}
.step{width:248px;height:248px;border-radius:50%;background:var(--circle);padding-top:30px;font-size:14.5px;line-height:20px}
.step h3{font-family:"Montserrat",sans-serif;font-weight:900;color:var(--blue);font-size:14px;margin:14px 0 8px}

/* footer */
.site-footer{top:2412px;height:292px;background:var(--footer);color:var(--white);font-size:12px}
.foot-brand{position:absolute;left:130px;top:86px;display:flex;align-items:center;gap:12px;font-weight:800;font-size:28px;color:var(--blue)}
.foot-brand i{width:22px;height:22px;border-radius:50%;background:var(--purple);display:block}
.site-footer h4{font-family:"Mulish",sans-serif;font-weight:800;font-size:13px;text-transform:uppercase}
.foot-contact{position:absolute;left:465px;top:44px}
.contact-row{display:flex;gap:9px;align-items:center;margin-top:28px;line-height:16px}
.contact-row+.contact-row{margin-top:22px}
.contact-row svg{flex:none}
.foot-menu{position:absolute;left:736px;top:45px}
.foot-menu ul{list-style:none;margin-top:23px;line-height:20px;text-transform:uppercase}
.foot-follow{position:absolute;left:901px;top:45px}
.social{display:flex;gap:6px;margin-top:15px}
.social i{width:26px;height:26px;border-radius:50%;background:var(--white);display:block}
.foot-line{position:absolute;left:130px;right:130px;top:207px;height:1px;background:#3a3a3a}
.copyright{position:absolute;top:250px;width:100%;text-align:center}
</style>
</head>
<body>

<header class="section site-header">
  <div class="brand"><i></i>Brightpath Rovers</div>
  <div class="call">
    <svg width="26" height="26" viewBox="0 0 26 26" aria-hidden="true"><rect width="26" height="26" rx="6" fill="#0f4aa5"/><path d="M8 6l3 0 1.5 4-2 1.5a9 9 0 0 0 4 4L16 13.5l4 1.5v3c0 1-1 2-2 2A12 12 0 0 1 6 8c0-1 1-2 2-2z" fill="#fff"/></svg>
    <div><small>Call us</small><strong>+1 555 010 2040</strong></div>
  </div>
  <a class="btn" href="#schedule">Schedule today</a>
  <nav class="nav">
    <a class="active" href="#">Home</a><a href="#about">About us</a><a href="#services">Services</a><a href="#pricing">Pricing</a><a href="#contact">Contact us</a>
  </nav>
</header>

<section class="section hero" role="img" aria-label="Photo of a white mobile clinic truck with a blue stripe and fold-down steps">
  <h1>Offering flu and covid vaccinations</h1>
  <a class="btn" href="#schedule">Reserve your on-site mobile vaccine clinic today!</a>
  <div class="dots"><i></i><i></i><i class="on"></i><i></i><i></i></div>
</section>

<section class="section about" id="about">
  <div class="photo" role="img" aria-label="Photo of a smiling pharmacist working at a laptop among plants"></div>
  <div class="about-text">
    <h2 class="heading">About <span>us</span><i class="rule"></i></h2>
    <p>Brightpath Rovers, PLLC mission: Making the workplace a healthier place.</p>
    <p>To provide on-site wellness services to employers that simplify and streamline employee preventative health.</p>
    <p>Pharmacist owned and operated.</p>
    <p>Brightpath Rovers, PLLC was started by local, Washington state licensed pharmacist with over 15 years experience vaccinating patients. She is a highly skilled immunizer and enjoys interacting with patients while providing this important preventative health services. Her vaccination experience spans from individual patient vaccinations to large clinics during community outbreaks.</p>
    <a class="btn" href="#">Read more</a>
  </div>
</section>

<section class="section services" id="services">
  <div class="services-text">
    <h2 class="heading">Services<i class="rule"></i></h2>
    <ul>
      <li>Brightpath Rovers will come to you!</li>
      <li>No crowded waiting rooms, no long lines, no hassle!</li>
      <li>Hassle-free, streamlining the vaccination process ... provide this on-site service as part of your employee wellness package</li>
      <li>Serving employers who want to increase the health and Wellness of their workplace</li>
      <li>vaccines including seasonal flu, COVID,Pneumonia</li>
      <li>Ensure your employees and their families remain healthy this flu season. Host a flu shot clinic on site to help your employees get vaccinated. Provide this service as part of youremployeeWellness benefits package.</li>
    </ul>
    <a class="btn" href="#">Read more</a>
  </div>
  <div class="photo" role="img" aria-label="Photo of several hands forming a heart shape"></div>
</section>

<section class="section band" id="pricing">
  <h2>Hassle-free, streamlining the vaccination process ...</h2>
  <p>Price quote is simple! No hidden travel/mileage calculations, no hidden hourly fees.</p>
  <a class="btn" href="#">Read more</a>
</section>

<section class="section schedule" id="schedule">
  <h2 class="heading">Schedule <span>today</span></h2>
  <p class="lead">Hassle-free, streamlining the vaccination process ...<br>Submit this simple Vaccine Clinic Needs Questionnaire and Brightpath Rovers will do the rest</p>
  <div class="short-rule"></div>
  <div class="steps">
    <div class="step">
      <svg width="50" height="60" viewBox="0 0 50 60" aria-hidden="true"><rect x="3" y="6" width="44" height="52" rx="3" fill="none" stroke="#a0479e" stroke-width="4"/><rect x="16" y="2" width="18" height="8" rx="2" fill="#a0479e"/><path d="M17 22l6 6 10-11" fill="none" stroke="#a0479e" stroke-width="4"/><path d="M12 38h4M20 38h18M12 46h4M20 46h18" stroke="#a0479e" stroke-width="3"/></svg>
      <h3>STEP 1</h3>
      <p>Submit Vaccine Clinic<br>Needs Questionnaire.</p>
    </div>
    <div class="step">
      <svg width="54" height="60" viewBox="0 0 54 60" aria-hidden="true"><path d="M8 6h10l4 12-6 5a30 30 0 0 0 14 16l5-6 12 4v10c0 4-3 7-7 7C20 54 2 36 2 12c0-4 2-6 6-6z" fill="#a0479e"/><path d="M32 6a18 18 0 0 1 16 16M32 14a10 10 0 0 1 8 8" fill="none" stroke="#a0479e" stroke-width="4"/></svg>
      <h3>STEP 2</h3>
      <p>Brightpath Rovers, PLLC will<br>contact you to schedule<br>on-site vaccine clinic.</p>
    </div>
    <div class="step">
      <svg width="64" height="62" viewBox="0 0 64 62" aria-hidden="true"><g transform="rotate(-45 32 31)"><rect x="20" y="20" width="26" height="14" fill="#a0479e"/><rect x="46" y="24" width="8" height="6" fill="#a0479e"/><rect x="54" y="21" width="4" height="12" fill="#a0479e"/><path d="M20 27H4" stroke="#a0479e" stroke-width="3"/><rect x="14" y="21" width="4" height="12" fill="#a0479e"/></g></svg>
      <h3>STEP 3</h3>
      <p>Prepare your employees for<br>vaccine clinic day.</p>
    </div>
  </div>
</section>

<footer class="section site-footer" id="contact">
  <div class="foot-brand"><i></i>Brightpath Rovers</div>
  <div class="foot-contact">
    <h4>Contact us</h4>
    <div class="contact-row">
      <svg width="24" height="24" viewBox="0 0 24 24" aria-hidden="true"><circle cx="12" cy="12" r="12" fill="#fff"/><path d="M8 7h2l1 3-1.5 1a6 6 0 0 0 3 3L14 13l3 1v2c0 .6-.5 1-1 1A9 9 0 0 1 7 8c0-.6.4-1 1-1z" fill="#1d1d1d"/></svg>
      <div>Call Us<br>+1 555 010 2040</div>
    </div>
    <div class="contact-row">
      <svg width="24" height="24" viewBox="0 0 24 24" aria-hidden="true"><circle cx="12" cy="12" r="12" fill="#fff"/><rect x="7" y="8.5" width="10" height="7" fill="#1d1d1d"/><path d="M7 9l5 4 5-4" fill="none" stroke="#fff" stroke-width="1"/></svg>
      <div>E mail Us<br>info@brightpathrovers.com</div>
    </div>
  </div>
  <div class="foot-menu">
    <h4>Menu</h4>
    <ul><li>Home</li><li>About us</li><li>Services</li><li>Pricing</li><li>Contact us</li></ul>
  </div>
  <div class="foot-follow">
    <h4>Follow us</h4>
    <div class="social"><i aria-label="Social profile"></i><i aria-label="Social profile"></i><i aria-label="Social profile"></i></div>
  </div>
  <div class="foot-line"></div>
  <p class="copyright">Copyright © 2022 All Rights Reserved</p>
</footer>

</body>
</html>
```